Business Card for KV

We need a double sided business card:

First Name Last Name
Cell 123-456-7890
firstname@emailaddress.com

License #1234-ABCD-4567
WFRSL # 12345
Brookmere County

```html
<!DOCTYPE html>
<html lang="en">
<head>
<meta charset="utf-8">
<title>Kindred Valley – Business Card</title>
<link href="https://fonts.googleapis.com/css2?family=Fjalla+One&family=Poppins:wght@400&display=swap" rel="stylesheet">
<style>
  :root {
    --backdrop: #dcdcdc;
    --navy: #2e4e69;
    --olive: #9b9a3c;
    --paper: #ffffff;
    --ink: #3c4a5a;
  }
  html, body {
    margin: 0;
    width: 1200px;
    height: 800px;
    overflow: hidden;
    background: var(--backdrop);
  }
  .canvas {
    position: relative;
    width: 1200px;
    height: 800px;
  }
  .card {
    position: absolute;
    top: 283px;
    width: 430px;
    height: 238px;
    overflow: hidden;
  }
  .card--front { left: 111px; background: var(--paper); }
  .card--back  { left: 638px; background: var(--navy); }

  .brand {
    position: absolute;
    display: flex;
    align-items: center;
    gap: 8px;
    font-family: "Fjalla One", sans-serif;
    text-transform: uppercase;
    letter-spacing: 1px;
    white-space: nowrap;
  }
  .brand__dot {
    border-radius: 50%;
    background: var(--olive);
    flex: none;
  }
  .card--front .brand {
    left: 28px;
    top: 103px;
    font-size: 22px;
    color: var(--navy);
  }
  .card--front .brand__dot { width: 22px; height: 22px; }

  .card--back .brand {
    left: 50%;
    top: 50%;
    transform: translate(-50%, -50%);
    font-size: 34px;
    color: var(--paper);
    gap: 12px;
  }
  .card--back .brand__dot { width: 34px; height: 34px; }

  .divider {
    position: absolute;
    left: 219px;
    top: 72px;
    width: 1px;
    height: 96px;
    background: var(--navy);
  }

  .contact {
    position: absolute;
    left: 239px;
    top: 73px;
    font-family: "Poppins", sans-serif;
    font-size: 10px;
    line-height: 13px;
    color: var(--ink);
  }
  .contact__name {
    margin: 0 0 5px;
    font-family: "Fjalla One", sans-serif;
    font-weight: 400;
    font-size: 17px;
    line-height: 20px;
    color: var(--navy);
    letter-spacing: 0.3px;
  }
  .contact__name-last { color: var(--olive); }
  .contact__row {
    display: flex;
    align-items: center;
    gap: 5px;
    margin: 0 0 1px;
  }
  .contact__icon { width: 11px; height: 11px; flex: none; }
  .contact__meta { margin: 6px 0 0; }
  .contact__meta p { margin: 0; }
</style>
</head>
<body>
<main class="canvas">

  <section class="card card--front" aria-label="Card front">
    <div class="brand">
      <span class="brand__dot" aria-hidden="true"></span>
      <span class="brand__name">Kindred Valley</span>
    </div>

    <div class="divider" aria-hidden="true"></div>

    <div class="contact">
      <h1 class="contact__name">JORDAN <span class="contact__name-last">PELL</span></h1>
      <p class="contact__row">
        <svg class="contact__icon" viewBox="0 0 12 12" aria-hidden="true">
          <circle cx="6" cy="6" r="6" fill="var(--olive)"/>
          <path d="M4 3.2c.3-.2.6-.1.8.2l.5.8c.1.3 0 .5-.2.7l-.3.2c.3.7.8 1.2 1.5 1.5l.2-.3c.2-.2.4-.3.7-.2l.8.5c.3.2.4.5.2.8l-.3.4c-.3.3-.8.4-1.3.2C5 7.4 4.2 6.6 3.6 5 3.4 4.5 3.5 4 3.7 3.6z" fill="#fff"/>
        </svg>
        123-456-7890
      </p>
      <p class="contact__row">
        <svg class="contact__icon" viewBox="0 0 12 12" aria-hidden="true">
          <circle cx="6" cy="6" r="6" fill="var(--olive)"/>
          <rect x="3" y="4" width="6" height="4.2" rx="0.5" fill="#fff"/>
          <path d="M3.2 4.3 6 6.4l2.8-2.1" fill="none" stroke="var(--olive)" stroke-width="0.7"/>
        </svg>
        firstname@emailaddress.com
      </p>
      <div class="contact__meta">
        <p>License #1234-ABCD-4567</p>
        <p>WFRSL # 12345</p>
        <p>Brookmere County</p>
      </div>
    </div>
  </section>

  <section class="card card--back" aria-label="Card back">
    <div class="brand">
      <span class="brand__dot" aria-hidden="true"></span>
      <span class="brand__name">Kindred Valley</span>
    </div>
  </section>

</main>
</body>
</html>
```